Prepare boat for season

Heron Point Marina is a full service marina on Lake Tessaway, Arkansas.
The boats on our lake are primarily pontoons, ski boats and fishing boats.

I want to send a postcard out to our current customers and also to potential new customers reminding them to get their boat/motors serviced and ready for the warm weather that is just around the corner. This would be a reminder postacard but also to pickup some new business.

Some of the services that should be done are fluid changes, filters, water pump impellers, spark plugs, batteries and props.

Heron Point Marina has a Orvane certified mechanic on staff and we work on inboard and outboard motors.

I am looking for a clean, simple postcard.

Target Market(s)

Boat owners

Industry/Entity Type

Business

Font styles to use
Serif

Colors

Designer to choose colors to be used in the design.

Requirements
Must have
• Would like to list the bullet points of maintenance to be done: Fluid and filter change, etc.
Business Telephone Number and address

```html
<!DOCTYPE html>
<html lang="en">
<head>
<meta charset="utf-8">
<title>Heron Point Marina – Seasonal Service Postcard</title>
<link rel="stylesheet" href="https://fonts.googleapis.com/css2?family=Crimson+Pro:ital,wght@0,400;0,500;0,600;0,700;1,700&display=swap">
<style>
  :root {
    --page-bg: #e9e6e1;
    --brand-red: #e0262b;
    --brand-navy: #23306f;
    --ribbon-blue: #1466a6;
    --sky-top: #2e86d0;
    --sky-mid: #7fc0ec;
    --water: #9fd3e6;
    --water-deep: #3f8fb0;
    --shore: #3e6a2a;
    --white: #ffffff;
  }
  * { box-sizing: border-box; margin: 0; padding: 0; }
  html, body { width: 1200px; height: 675px; overflow: hidden; }
  body {
    background: var(--page-bg);
    font-family: "Crimson Pro", Georgia, serif;
    position: relative;
  }
  .postcard {
    position: absolute;
    top: 125px;
    width: 555px;
    height: 428px;
    overflow: hidden;
    box-shadow: 0 4px 14px rgba(0,0,0,0.25);
  }
  .postcard--front { left: 32px; }
  .postcard--back { left: 612px; background: var(--white); }

  /* Front */
  .front-photo {
    position: absolute; inset: 0;
    background: linear-gradient(180deg, var(--sky-top) 0%, var(--sky-mid) 36%, var(--shore) 37%, var(--shore) 39%, var(--water) 40%, var(--water-deep) 100%);
  }
  .front-lockup {
    position: absolute;
    left: 349px;
    bottom: 22px;
    color: var(--white);
  }
  .front-lockup .brand-name {
    font-size: 30px;
    font-weight: 600;
    line-height: 30px;
    width: 200px;
  }
  .front-lockup .brand-place {
    font-size: 17px;
    line-height: 18px;
    margin-top: 4px;
  }

  /* Back */
  .back-sky {
    position: absolute; inset: 0;
    background: linear-gradient(90deg, var(--white) 0%, var(--white) 42%, #d6ebf8 64%, var(--sky-mid) 100%);
  }
  .brand-lockup {
    position: absolute;
    left: 16px; top: 17px;
    width: 280px;
  }
  .brand-lockup .brand-mark {
    display: inline-block;
    width: 13px; height: 13px;
    background: var(--brand-red);
    border-radius: 50%;
    margin-right: 8px;
    vertical-align: 3px;
  }
  .brand-lockup .brand-name {
    font-size: 30px;
    font-weight: 700;
    color: var(--brand-red);
    line-height: 30px;
  }
  .brand-lockup .brand-place {
    color: var(--brand-navy);
    font-size: 17px;
    line-height: 18px;
    margin: 4px 0 0 21px;
  }
  .services-title {
    position: absolute;
    left: 16px; top: 138px;
    color: var(--brand-red);
    font-size: 14px;
    line-height: 18px;
    font-weight: 700;
  }
  .services-list {
    position: absolute;
    left: 16px; top: 158px;
    list-style: none;
    color: var(--brand-red);
    font-size: 13.5px;
    line-height: 16.6px;
  }
  .services-list li::before { content: "\2022\00a0"; }
  .mechanic-note {
    position: absolute;
    left: 16px; top: 282px;
    width: 285px;
    color: var(--brand-navy);
    font-size: 13.5px;
    line-height: 16.4px;
  }
  .ribbon {
    position: absolute;
    left: 0; top: 337px;
    width: 316px; height: 67px;
  }
  .ribbon svg { position: absolute; inset: 0; }
  .ribbon-text {
    position: absolute;
    left: 14px; top: 8px;
    width: 270px;
    color: var(--white);
    font-size: 15px;
    font-weight: 500;
    line-height: 17px;
  }
  .contact {
    position: absolute;
    right: 17px; bottom: 18px;
    text-align: right;
    color: var(--brand-navy);
    font-size: 14px;
    font-weight: 700;
    font-style: italic;
    line-height: 18px;
  }
</style>
</head>
<body>
  <section class="postcard postcard--front">
    <div class="front-photo" role="img" aria-label="Photo of a pontoon boat with an outboard motor cruising on a calm lake under a blue sky with clouds and a wooded shoreline"></div>
    <div class="front-lockup">
      <div class="brand-name">Heron Point Marina</div>
      <div class="brand-place">Lake Tessaway<br>Arkansas</div>
    </div>
  </section>

  <section class="postcard postcard--back">
    <div class="back-sky" role="img" aria-label="Soft blue sky with light clouds fading to white"></div>
    <div class="brand-lockup">
      <div><span class="brand-mark"></span><span class="brand-name">Heron Point<br>Marina</span></div>
      <div class="brand-place">Lake Tessaway<br>Arkansas</div>
    </div>
    <h2 class="services-title">Services offered:</h2>
    <ul class="services-list">
      <li>fluid changes</li>
      <li>filters</li>
      <li>water</li>
      <li>pump impellers</li>
      <li>spark plugs</li>
      <li>batteries</li>
      <li>props.</li>
    </ul>
    <p class="mechanic-note">Heron Point Marina has an Orvane certified mechanic on staff and we work on inboard and outboard motors.</p>
    <div class="ribbon">
      <svg viewBox="0 0 316 67" width="316" height="67" aria-hidden="true">
        <polygon points="0,0 316,0 300,33.5 316,67 0,67" fill="var(--ribbon-blue)"/>
      </svg>
      <p class="ribbon-text">So get your boat/motors serviced and ready for the warm weather that is just around the corner!</p>
    </div>
    <address class="contact">(342) 555 0187<br>Lake Tessaway, Arkansas</address>
  </section>
</body>
</html>
```